Diabetes Education Flyer Design Project

We need a 8.5" X 11" flyer design for a retail pharmacy located in Queens, NYC to promote our new program of "Free Diabetes Education". This flyer will be distributed to doctors offices and to places where people congregate. The flyer should create a fear to the audience about diabetes and an urgency to come or call the pharmacy to get more information on the "Free Diabetes Education". The target audience is 40+ years old with national background of West Indies and India. They are mostly blue color worker with a highschool or less education

Target Market(s)

People with diabetes aging 40+, from West Indies and India, low literacy level

Industry/Entity Type

Education

Requirements
Must have
• Must have graphics and colors to attract the targetted age/race/literacy. Must have graphics and colors to create fear at the begining and hope at the end.
Nice to have
• Fonts to support the theme

```html
<!DOCTYPE html>
<html lang="en">
<head>
<meta charset="utf-8">
<title>Diabetes Kills – Free Diabetes Education Flyer</title>
<link rel="stylesheet" href="https://fonts.googleapis.com/css2?family=Archivo+Black&family=Oswald:wght@700&family=Questrial&family=Roboto+Condensed:wght@700&display=swap">
<style>
  :root {
    --alarm-red: #e4002b;
    --brand-red: #e8284a;
    --ink: #111111;
    --paper: #ffffff;
    --photo-dark: #3a3a3a;
    --photo-mid: #9a9a9a;
    --photo-light: #e6e6e6;
  }
  * { margin: 0; padding: 0; box-sizing: border-box; }
  html, body { width: 848px; height: 1200px; overflow: hidden; background: var(--paper); }
  .flyer {
    position: relative;
    width: 848px;
    height: 1200px;
    overflow: hidden;
    background: var(--paper);
    font-family: "Questrial", sans-serif;
  }
  .portrait-area {
    position: absolute;
    left: 0; top: 0;
    width: 520px; height: 1065px;
    background:
      radial-gradient(ellipse 260px 420px at 170px 560px, var(--photo-mid) 0%, rgba(154,154,154,0.6) 55%, rgba(255,255,255,0) 100%),
      linear-gradient(90deg, var(--photo-dark) 0%, var(--photo-mid) 35%, var(--photo-light) 70%, rgba(255,255,255,0) 100%);
  }
  .headline {
    position: absolute;
    right: 14px;
    font-family: "Archivo Black", sans-serif;
    color: var(--alarm-red);
    line-height: 1;
    text-align: right;
    letter-spacing: -2px;
  }
  .headline--diabetes { top: 6px; font-size: 138px; right: 12px; }
  .headline--kills { top: 122px; font-size: 156px; }
  .statistic {
    position: absolute;
    right: 26px;
    top: 278px;
    font-family: "Oswald", sans-serif;
    font-weight: 700;
    font-size: 104px;
    line-height: 1;
    color: var(--ink);
  }
  .statistic-label {
    position: absolute;
    right: 26px;
    top: 418px;
    font-family: "Roboto Condensed", sans-serif;
    font-weight: 700;
    font-size: 46px;
    color: var(--ink);
  }
  .question {
    position: absolute;
    left: 400px;
    width: 430px;
    text-align: center;
    color: var(--alarm-red);
    font-size: 94px;
    line-height: 1;
  }
  .question--one { top: 502px; }
  .question--two { top: 608px; }
  .brand {
    position: absolute;
    left: 430px;
    top: 740px;
    display: flex;
    align-items: center;
    gap: 14px;
  }
  .brand-mark {
    width: 30px; height: 30px;
    border-radius: 50%;
    background: var(--brand-red);
  }
  .brand-name {
    font-size: 54px;
    color: var(--brand-red);
    line-height: 1;
  }
  .offer {
    position: absolute;
    right: 30px;
    top: 840px;
    text-align: right;
    color: var(--alarm-red);
    font-size: 54px;
    line-height: 0.95;
  }
  .offer-free { font-family: "Archivo Black", sans-serif; font-size: 50px; }
  .call-to-action {
    position: absolute;
    right: 30px;
    top: 990px;
    text-align: right;
    color: var(--ink);
    font-size: 24px;
    line-height: 1.2;
  }
  .contact-band {
    position: absolute;
    left: 0; top: 1065px;
    width: 848px; height: 98px;
    background: var(--alarm-red);
    color: var(--paper);
    display: flex;
    align-items: center;
    justify-content: space-between;
    padding: 0 34px 0 22px;
  }
  .contact-address { font-size: 28px; line-height: 1.15; }
  .contact-phone { font-size: 56px; }
  .footnote {
    position: absolute;
    right: 24px;
    top: 1170px;
    width: 420px;
    text-align: right;
    font-size: 8.5px;
    line-height: 1.2;
    color: var(--ink);
  }
</style>
</head>
<body>
<main class="flyer">
  <div class="portrait-area" role="img" aria-label="Black and white close-up photograph of a worried woman with a tear running down her cheek"></div>

  <h1>
    <span class="headline headline--diabetes">DIABETES</span>
    <span class="headline headline--kills">KILLS</span>
  </h1>
  <p class="statistic">3,400,000</p>
  <p class="statistic-label">People In a Year*</p>

  <p class="question question--one">Are You</p>
  <p class="question question--two">the Next?</p>

  <div class="brand">
    <span class="brand-mark"></span>
    <span class="brand-name">Harbor Pharmacy</span>
  </div>

  <p class="offer">Is Offering <span class="offer-free">FREE</span><br>Education<br>for Diabetics</p>

  <p class="call-to-action">Call or Stop by Now! Your Life Depends<br>on It! Educate Yourself and Live Longer</p>

  <footer class="contact-band">
    <address class="contact-address" style="font-style:normal">48-20 Maple Ave.,<br>Queens, NY 11400</address>
    <span class="contact-phone">(718) 555-0142</span>
  </footer>

  <p class="footnote">*According to World Health Organization in 2004, an estimated 3.4 million people died worldwide from consequences of high blood sugar. Fact Sheet No. 312 (August, 2011)</p>
</main>
</body>
</html>
```